Need *Plum Crafted* Events Company Website
Bright Harbor Gatherings Website
Need *Plum Crafted* Events Company Website - Events
Creative Brief
Events
www.brightharborgatherings.example
Bright Harbor Gatherings (BHG) is a multi-dimensional event management firm providing all aspects of support and expertise for any special event. By providing upscale and individualized service, our events are unique and tailored around your personal vision, style and budget.
We provide partial and full-service event coordination services for all types of events; specializing in corporate meetings, conferences, receptions, and everyday social events.
We like unique and captivating web design that illustrates the characteristics of our brand and service offerrings. Our logo speaks to a company that is unique and classy with an edge. DISLIKE: Black or extremely dark backgrounds. Too fancy flash applications, Music or any kind of intro, anything that is too elaborate. LIKE: Easy flow and simplicity. I like the mix of soft neutrals
Feminine
neutral tones
pop of red
complementary tones
right side
www.vowlantern.example
www.quillaffairs.example
Will attached websites that we like later Please use the Fonts from my logo: Will attach files I would like for you to use the accent color on my logo as an special accent only so my logo is not overpowered. I am open to navigation placement but it does not give me that option so I selected what I believe is my personal preference.

```html
<!DOCTYPE html>
<html lang="en">
<head>
<meta charset="utf-8">
<title>Bright Harbor Gatherings</title>
<link rel="stylesheet" href="https://fonts.googleapis.com/css2?family=Great+Vibes&family=Open+Sans:ital,wght@0,400;0,600;1,400;1,700&display=swap">
<style>
  :root {
    --plum-bg: #6d4851;
    --plum-deep: #4f3039;
    --cream: #efe6d8;
    --cream-dark: #e2d4c0;
    --stripe: #d9c3b4;
    --accent-red: #c8242f;
    --brand-ink: #6b3d49;
    --white: #ffffff;
    --text-soft: #f3ece6;
    --footer-text: #e8d9d4;
    --go-green: #3f9b2f;
    --caption-ink: #3a2a2c;
    --contact-ink: #8a7a74;
  }
  * { margin: 0; padding: 0; box-sizing: border-box; }
  html, body { width: 1200px; height: 799px; overflow: hidden; }
  body {
    position: relative;
    background: radial-gradient(ellipse at 60% 40%, #7a545d 0%, var(--plum-bg) 55%, var(--plum-deep) 100%);
    font-family: "Open Sans", Arial, sans-serif;
  }
  .sidebar {
    position: absolute; left: 101px; top: 0; width: 264px; height: 799px;
    background: linear-gradient(180deg, var(--cream) 0%, var(--cream-dark) 100%);
    box-shadow: 0 0 14px rgba(0,0,0,.35);
    overflow: hidden;
  }
  .sidebar::after {
    content: ""; position: absolute; right: 0; top: 0; width: 12px; height: 100%;
    background: repeating-linear-gradient(90deg, var(--stripe) 0 2px, var(--cream) 2px 4px);
  }
  .brand {
    position: absolute; left: 0; top: 60px; width: 252px; text-align: center;
  }
  .brand-mark {
    width: 70px; height: 70px; border-radius: 50%; background: var(--brand-ink);
    margin: 0 auto 26px;
  }
  .brand-name {
    font-family: "Great Vibes", cursive; font-size: 44px; line-height: 1.05;
    color: var(--brand-ink);
  }
  .main-nav {
    position: absolute; left: 0; top: 392px; width: 252px; list-style: none; text-align: center;
  }
  .main-nav li {
    font-family: "Great Vibes", cursive; font-size: 31px; line-height: 41px; color: var(--accent-red);
  }
  .contact {
    position: absolute; left: 48px; top: 708px; width: 200px;
    font-size: 11.5px; color: var(--contact-ink); white-space: nowrap;
  }
  .contact p { display: flex; align-items: center; gap: 8px; height: 26px; }
  .contact svg { flex: none; }
  .connect {
    position: absolute; left: 826px; top: 22px; display: flex; align-items: center; gap: 6px;
    font-style: italic; font-size: 16px; color: var(--text-soft);
  }
  .connect span.gap { width: 8px; }
  .social { width: 22px; height: 22px; border-radius: 3px; background: #4a78c0; }
  .social.second { background: #3fb6e6; }
  .social.third { background: #2e6fb0; }
  .stage {
    position: absolute; left: 372px; top: 72px; width: 727px; height: 629px;
    background: var(--white); padding: 10px;
    box-shadow: 0 4px 14px rgba(0,0,0,.4);
  }
  .stage-photo {
    width: 100%; height: 100%;
    background: linear-gradient(135deg, #c9b59a 0%, #8a6e58 35%, #5c4a40 60%, #a68f7c 100%);
  }
  .welcome {
    position: absolute; left: 257px; top: 60px; width: 451px; height: 204px;
    background: rgba(255,255,255,.28); border: 1px solid rgba(255,255,255,.6);
    border-radius: 10px; padding: 14px 18px; color: var(--white);
    font-style: italic; font-size: 12.5px; line-height: 16px;
    text-shadow: 0 1px 2px rgba(0,0,0,.5);
  }
  .welcome h1 { font-size: 20px; font-weight: 700; font-style: italic; margin-bottom: 6px; }
  .welcome p { margin-bottom: 8px; }
  .play-intro {
    position: absolute; right: 22px; bottom: 10px; width: 132px; height: 31px;
    border-radius: 16px; background: linear-gradient(180deg, #6fcb4a, var(--go-green));
    color: var(--white); font-size: 12px; font-weight: 600; font-style: normal;
    display: flex; align-items: center; justify-content: center; gap: 7px;
  }
  .services { position: absolute; left: 24px; top: 468px; display: flex; gap: 38px; }
  .service {
    width: 197px; height: 144px; background: var(--white); padding: 6px;
    box-shadow: 0 3px 8px rgba(0,0,0,.4); position: relative;
  }
  .service-photo { width: 100%; height: 100%; }
  .service-photo.meetings { background: linear-gradient(135deg, #a3a3a8, #3b3a44); }
  .service-photo.seminars { background: linear-gradient(135deg, #c7a770, #6c5a48); }
  .service-photo.weddings { background: linear-gradient(135deg, #b7a6cf, #f0eef4); }
  .service-caption {
    position: absolute; left: 6px; right: 6px; bottom: 6px; height: 34px;
    background: rgba(255,255,255,.85); text-align: center; white-space: nowrap;
    font-family: "Great Vibes", cursive; font-size: 21px; line-height: 34px; color: var(--caption-ink);
  }
  .footer-nav, .copyright {
    position: absolute; top: 762px; font-size: 10.5px; color: var(--footer-text);
  }
  .footer-nav { left: 396px; }
  .copyright { right: 110px; }
</style>
</head>
<body>
  <aside class="sidebar">
    <div class="brand">
      <div class="brand-mark"></div>
      <div class="brand-name">Bright Harbor<br>Gatherings</div>
    </div>
    <ul class="main-nav">
      <li>Home</li>
      <li>About Us</li>
      <li>Services</li>
      <li>Contact Us</li>
      <li>Events</li>
      <li>Our Blog</li>
    </ul>
    <div class="contact">
      <p><svg width="16" height="14" viewBox="0 0 16 14"><path d="M2 4 Q8 0 14 4 L12 6 L10 5 L10 4 Q8 3 6 4 L6 5 L4 6 Z M3 8 H13 V13 H3 Z" fill="#8a7a74"/></svg>(555) - 214 - 7380</p>
      <p><svg width="16" height="12" viewBox="0 0 16 12"><rect x="0.5" y="0.5" width="15" height="11" fill="none" stroke="#8a7a74"/><path d="M1 1 L8 7 L15 1" fill="none" stroke="#8a7a74"/></svg>info@brightharbor.example</p>
    </div>
  </aside>

  <div class="connect">
    Connect with us :<span class="gap"></span>
    <span class="social"></span><span class="social second"></span><span class="social third"></span>
  </div>

  <main class="stage">
    <div class="stage-photo" role="img" aria-label="Elegant banquet table set with glassware, napkins and candles"></div>
    <section class="welcome">
      <h1>Welcome to Bright Harbor Gatherings</h1>
      <p>Bright Harbor Gatherings (BHG) is a multi-dimensional event management firm providing all aspects of support and expertise for any special event. By providing upscale and individualized service, our events are unique and tailored around your personal vision, style and budget.</p>
      <p>We provide partial and full-service event coordination services for all types of events; specializing in corporate meetings, conferences, receptions, and everyday social events.</p>
      <div class="play-intro">
        <svg width="12" height="12" viewBox="0 0 12 12"><circle cx="6" cy="6" r="6" fill="#fff"/><path d="M4.5 3 L9 6 L4.5 9 Z" fill="#3f9b2f"/></svg>
        PLAY INTRO
      </div>
    </section>
    <div class="services">
      <div class="service">
        <div class="service-photo meetings" role="img" aria-label="Business team gathered around a meeting table"></div>
        <div class="service-caption">Corporate Meetings</div>
      </div>
      <div class="service">
        <div class="service-photo seminars" role="img" aria-label="Conference hall with rows of seated attendees"></div>
        <div class="service-caption">Seminars &amp; Conferences</div>
      </div>
      <div class="service">
        <div class="service-photo weddings" role="img" aria-label="Reception hall decorated with white and lavender draping"></div>
        <div class="service-caption">Weddings &amp; Receptions</div>
      </div>
    </div>
  </main>

  <nav class="footer-nav">Home | About us | Services | Contact us | Events | Our Blog</nav>
  <p class="copyright">Copyright © 2011, Bright Harbor Gatherings. All rights reserved.</p>
</body>
</html>
```